1200mm high x 900mm wide kids fitness poster for gym

I need an a poster designed to promote my kids/teenagers class.

This class is aimed at parents with kids between 10-15.

Design should be friendly and modern

Class is designed for kids that play sport and want to improve their fitness

Industry/Entity Type

Fitness

Font styles to use
Sans Serif

Colors

Designer to choose colors to be used in the design.

Requirements
Must have
• Text:
• Bright Stride teens program (TITLE)
• Improve: Performance, health, fitness, confidence, team mentality (BULLET POINTS)
• They will love our teen program! Contact us now to find out more:
• 1300452198
• enquiries@brightstride.fitness
• www.brightstride.fitness
• Must have friendly image of kids fitness or sport (FUN AND FRIENDLY IMAGE)

```html
<!DOCTYPE html>
<html lang="en">
<head>
<meta charset="utf-8">
<title>Bright Stride Teens Program Poster</title>
<link href="https://fonts.googleapis.com/css2?family=Montserrat:wght@900&family=Roboto:ital,wght@0,300;0,400;0,500;0,700;1,700;1,900&display=swap" rel="stylesheet">
<style>
  :root {
    --brand-blue: #1d5c9c;
    --band-grey: #dcdcdc;
    --ink: #1d1d1d;
    --sky-top: #ffffff;
    --sky-mid: #d8eefa;
    --sky-low: #a9d8f3;
    --hill: #3a6d97;
    --hill-dark: #2a5479;
    --footer-deep: #1f3a55;
    --footer-base: #2d5b82;
    --accent-cyan: #45b8ea;
    --white: #ffffff;
    --page-bg: #e9ebee;
  }
  * { margin: 0; padding: 0; box-sizing: border-box; }
  html, body { width: 1200px; height: 1200px; overflow: hidden; background: var(--page-bg); }
  .poster {
    position: absolute; left: 150px; top: 0; width: 900px; height: 1200px; overflow: hidden;
    background: linear-gradient(180deg, var(--sky-top) 0%, var(--sky-top) 22%, var(--sky-mid) 38%, var(--sky-low) 75%, var(--sky-mid) 100%);
    font-family: "Roboto", sans-serif;
  }
  .poster-art { position: absolute; inset: 0; }
  .brand-mark {
    position: absolute; left: 0; width: 900px; top: 65px; text-align: center;
    font-family: "Roboto", sans-serif; font-weight: 700; font-size: 16px; letter-spacing: 1px;
    line-height: 1; color: var(--brand-blue); white-space: nowrap;
  }
  .title {
    position: absolute; left: 0; width: 900px; top: 150px; text-align: center;
    font-family: "Montserrat", sans-serif; font-weight: 900; font-size: 70px; line-height: 1;
    color: var(--brand-blue); letter-spacing: 1px;
  }
  .subtitle {
    position: absolute; left: 0; width: 900px; top: 226px; text-align: center;
    font-family: "Roboto", sans-serif; font-weight: 300; font-size: 60px; line-height: 1;
    color: var(--ink);
  }
  .benefit {
    position: absolute; font-family: "Roboto", sans-serif; font-style: italic; font-weight: 700;
    font-size: 29px; color: var(--brand-blue); line-height: 1; white-space: nowrap;
  }
  .benefit-performance { left: 625px; top: 538px; }
  .benefit-health { left: 429px; top: 620px; }
  .benefit-fitness { left: 360px; top: 731px; }
  .benefit-confidence { left: 355px; top: 845px; }
  .benefit-team { left: 503px; top: 921px; word-spacing: 8px; }
  .cta { position: absolute; left: 53px; top: 1060px; color: var(--white); }
  .cta-lead { font-size: 21px; font-weight: 400; }
  .cta-highlight { font-size: 28px; font-weight: 700; color: var(--accent-cyan); margin-top: 2px; }
  .cta-note { font-size: 17px; font-weight: 400; margin-top: 4px; }
  .contact { position: absolute; left: 600px; top: 1061px; color: var(--white); }
  .contact-phone { font-size: 30px; font-style: italic; font-weight: 900; letter-spacing: 0.5px; }
  .contact-line { font-size: 17px; font-weight: 400; margin-top: 4px; }
</style>
</head>
<body>
<div class="poster">
  <svg class="poster-art" width="900" height="1200" viewBox="0 0 900 1200">
    <defs>
      <linearGradient id="hill-fill" x1="0" y1="0" x2="0" y2="1">
        <stop offset="0" stop-color="var(--hill)"/>
        <stop offset="1" stop-color="var(--hill-dark)"/>
      </linearGradient>
      <radialGradient id="runner-glow" cx="0.5" cy="0.5" r="0.5">
        <stop offset="0" stop-color="#ffffff" stop-opacity="0.85"/>
        <stop offset="1" stop-color="#ffffff" stop-opacity="0"/>
      </radialGradient>
      <linearGradient id="photo-grass" x1="0" y1="0" x2="0" y2="1">
        <stop offset="0" stop-color="#9fb8a4"/><stop offset="1" stop-color="#5f8d3c"/>
      </linearGradient>
      <linearGradient id="photo-nature" x1="0" y1="0" x2="0" y2="1">
        <stop offset="0" stop-color="#b9cfd6"/><stop offset="1" stop-color="#6f8f4e"/>
      </linearGradient>
      <linearGradient id="photo-studio" x1="0" y1="0" x2="0" y2="1">
        <stop offset="0" stop-color="#f2f2f0"/><stop offset="1" stop-color="#d6d2cc"/>
      </linearGradient>
      <linearGradient id="photo-boxing" x1="0" y1="0" x2="0" y2="1">
        <stop offset="0" stop-color="#eeeeee"/><stop offset="1" stop-color="#d9b39c"/>
      </linearGradient>
      <linearGradient id="photo-team" x1="0" y1="0" x2="0" y2="1">
        <stop offset="0" stop-color="#c9d3cf"/><stop offset="0.45" stop-color="#b84a45"/><stop offset="1" stop-color="#5c8a38"/>
      </linearGradient>
    </defs>

    <!-- header band -->
    <polygon points="0,47 352,47 387,103 0,103" fill="var(--brand-blue)"/>
    <polygon points="548,47 900,47 900,103 513,103" fill="var(--brand-blue)"/>
    <polygon points="0,106 389,106 393,114 0,114" fill="var(--band-grey)"/>
    <polygon points="511,106 900,106 900,114 507,114" fill="var(--band-grey)"/>

    <!-- improve arc -->
    <path d="M 143 900 C 110 620, 320 355, 570 350 C 640 350, 700 365, 720 380" fill="none" stroke="var(--brand-blue)" stroke-width="5" stroke-linecap="round" opacity="0.85"/>
    <path id="improve-path" d="M 128 605 C 175 470, 290 370, 450 340" fill="none"/>
    <text font-family="Roboto, sans-serif" font-weight="300" font-size="46" fill="var(--brand-blue)">
      <textPath href="#improve-path" textLength="330" lengthAdjust="spacing">IMPROVE</textPath>
    </text>

    <!-- runner area -->
    <g role="img" aria-label="Faint silhouette of a running child in a team shirt">
      <ellipse cx="615" cy="790" rx="140" ry="220" fill="url(#runner-glow)" opacity="0.7"/>
    </g>

    <!-- hills -->
    <path d="M 0 808 C 40 830, 90 900, 159 912 C 260 930, 380 960, 470 985 C 600 1010, 760 990, 900 922 L 900 1200 L 0 1200 Z" fill="url(#hill-fill)" opacity="0.9"/>

    <!-- footer -->
    <rect x="0" y="1051" width="900" height="100" fill="var(--footer-deep)"/>
    <rect x="0" y="1151" width="900" height="49" fill="var(--footer-base)"/>

    <!-- brace -->
    <path d="M 590 1052 C 576 1052, 580 1070, 580 1085 C 580 1095, 576 1100, 568 1102 C 576 1104, 580 1109, 580 1119 C 580 1134, 576 1152, 590 1152" fill="none" stroke="var(--white)" stroke-width="2"/>

    <!-- photo circles -->
    <g role="img" aria-label="Photo of two teenage footballers chasing the ball">
      <circle cx="541" cy="490" r="93" fill="url(#photo-grass)" stroke="var(--white)" stroke-width="5"/>
    </g>
    <g role="img" aria-label="Photo of a smiling girl doing a yoga pose outdoors">
      <circle cx="348" cy="552" r="93" fill="url(#photo-nature)" stroke="var(--white)" stroke-width="5"/>
    </g>
    <g role="img" aria-label="Photo of a girl stretching on a gym mat">
      <circle cx="256" cy="730" r="93" fill="url(#photo-studio)" stroke="var(--white)" stroke-width="5"/>
    </g>
    <g role="img" aria-label="Photo of a boy raising his boxing gloves">
      <circle cx="263" cy="929" r="93" fill="url(#photo-boxing)" stroke="var(--white)" stroke-width="5"/>
    </g>
    <g role="img" aria-label="Photo of a youth football team in a huddle">
      <circle cx="441" cy="1022" r="93" fill="url(#photo-team)" stroke="var(--white)" stroke-width="5"/>
    </g>
  </svg>

  <div class="brand-mark">BRIGHT STRIDE</div>
  <h1 class="title">BRIGHT STRIDE</h1>
  <div class="subtitle">TEENS PROGRAM</div>

  <div class="benefit benefit-performance">PERFORMANCE</div>
  <div class="benefit benefit-health">HEALTH</div>
  <div class="benefit benefit-fitness">FITNESS</div>
  <div class="benefit benefit-confidence">CONFIDENCE</div>
  <div class="benefit benefit-team">TEAM MENTALITY</div>

  <div class="cta">
    <div class="cta-lead">THEY WILL LOVE OUR</div>
    <div class="cta-highlight">TEEN PROGRAM!</div>
    <div class="cta-note">CONTACT US NOW TO FIND OUT MORE:</div>
  </div>

  <div class="contact">
    <div class="contact-phone">1300452198</div>
    <div class="contact-line">enquiries@brightstride.fitness</div>
    <div class="contact-line">www.brightstride.fitness</div>
  </div>
</div>
</body>
</html>
```